Plumbing Company- Mass mailing Post card

Name of our company is Bramwell plumbing, Inc. Located in West Palm Beach, Florida. Tag line is "Our service is what set's us apart". We're looking for a postcard that we can send as a mass mailing (QPMX). Our clients are high end so we're looking for classy, simple, clean and easy to read (not busy), to represent the kind of work we do, (our work is like no other). Want an attention getter that manages to get the customer to turn the card over for more info.
Include: phone # 561-555-0193, website www.brwplumbing.example, License CFC9073651
Samples that can be included:
-Tap in to 30 plus years of experience.
-Our reputation is our best asset
-Call Bramwell Plumbing today and let us take care of your plumbing needs.
-Bramwell services offered
-We are the difference!
-Serving the Palm Beaches!

Target Market(s)

High end, owners and Property managers

Industry/Entity Type

Plumbing

Font styles to use
Serif

Requirements
Must have
• Tag line
• Classy and clean
Nice to have
• Our original logo color is blue/grey but not opposed if something different is suggested.
• Interested in seeing ideas
Should not have
• Not to be busy looking.

```html
<!DOCTYPE html>
<html lang="en">
<head>
<meta charset="utf-8">
<title>Bramwell Plumbing Postcard</title>
<link href="https://fonts.googleapis.com/css2?family=Cinzel:wght@400;500&family=Oswald:wght@400;500&family=Roboto:wght@400;500&family=Montserrat:wght@600&display=swap" rel="stylesheet">
<style>
  :root {
    --green-deep: #2f9e35;
    --green-mid: #4cb848;
    --green-light: #9bd67c;
    --ink: #111;
    --white: #fff;
    --silver: #c9cdd0;
    --backdrop: #e9e9e7;
    --gold-dark: #7a5a1c;
    --gold-light: #e2c071;
    --tile-light: #efe2cb;
    --tile-dark: #b79a73;
  }
  html, body { margin: 0; padding: 0; }
  body {
    width: 939px; height: 1200px; overflow: hidden;
    background: var(--backdrop);
    position: relative;
    font-family: "Roboto", Arial, sans-serif;
  }
  .card {
    position: absolute; left: 48px;
    width: 843px; height: 543px;
    overflow: hidden;
    box-shadow: 0 4px 14px rgba(0,0,0,.25);
    background: var(--white);
  }
  .card--front { top: 46px; }
  .card--back { top: 610px; }
  .card svg.art { position: absolute; inset: 0; }
  .brand { position: absolute; text-align: center; }
  .brand__name {
    font-family: "Montserrat", Arial, sans-serif; font-weight: 600;
    letter-spacing: 1px; color: #1d2733; line-height: 1;
    display: flex; align-items: center; gap: 10px;
  }
  .brand__dot { width: 26px; height: 26px; border-radius: 50%; background: #1d2733; flex: none; }
  .brand__sub {
    font-family: "Montserrat", Arial, sans-serif; font-weight: 600;
    color: #1d2733; letter-spacing: 5px; font-size: 12px; margin-top: 4px; padding-left: 36px;
  }
  .card--front .brand { left: 105px; top: 34px; }
  .card--front .brand__name { font-size: 28px; }
  .tagline {
    position: absolute; left: 0; width: 470px; text-align: center;
    font-family: "Cinzel", Georgia, serif; font-weight: 500; margin: 0;
  }
  .tagline--dark { top: 204px; font-size: 38px; color: var(--ink); }
  .tagline--light { top: 256px; font-size: 36px; color: var(--white); }
  .front-call {
    position: absolute; left: 0; width: 470px; text-align: center; top: 330px;
    font-size: 26px; color: var(--ink);
  }
  .website {
    position: absolute; color: var(--white); font-size: 15px; letter-spacing: 6px; font-weight: 500;
    white-space: nowrap;
  }
  .card--front .website { left: 0; width: 470px; text-align: center; top: 366px; }
  .license { position: absolute; right: 24px; bottom: 16px; font-size: 16px; color: var(--ink); }
  .call-badge {
    position: absolute; left: 369px; top: 187px; width: 142px; height: 142px;
    border-radius: 50%; background: var(--white);
    box-shadow: 0 0 0 5px var(--green-mid), 0 0 0 9px var(--silver);
    display: flex; flex-direction: column; align-items: center; justify-content: center;
    font-family: "Oswald", Arial, sans-serif; color: var(--ink); line-height: 1.15;
    white-space: nowrap;
  }
  .call-badge__label { font-size: 21px; }
  .call-badge__phone { font-size: 23px; font-weight: 500; letter-spacing: -0.6px; }
  .card--back .brand { left: 128px; top: 450px; }
  .card--back .brand__name { font-size: 24px; }
  .card--back .brand__dot { width: 22px; height: 22px; }
  .card--back .brand__sub { font-size: 11px; padding-left: 32px; }
  .card--back .website { left: 0; width: 430px; text-align: center; top: 502px; }
  .postage {
    position: absolute; left: 726px; top: 356px; width: 90px;
    border: 1px solid #222; font-size: 11px; line-height: 1.35; text-align: center; padding: 3px 0;
  }
  .address {
    position: absolute; left: 635px; top: 450px; width: 184px; height: 62px;
    border: 1px solid #222; font-size: 10px; line-height: 1.25; box-sizing: border-box; padding: 24px 10px 0;
  }
</style>
</head>
<body>

<section class="card card--front">
  <svg class="art" width="843" height="543" viewBox="0 0 843 543">
    <defs>
      <linearGradient id="frontGreen" x1="0" y1="0" x2="1" y2="1">
        <stop offset="0" stop-color="var(--green-mid)"/>
        <stop offset="0.5" stop-color="var(--green-light)"/>
        <stop offset="1" stop-color="var(--green-deep)"/>
      </linearGradient>
      <linearGradient id="goldPhoto" x1="0" y1="0" x2="1" y2="1">
        <stop offset="0" stop-color="#5a2a3a"/>
        <stop offset="0.45" stop-color="var(--gold-light)"/>
        <stop offset="0.8" stop-color="var(--gold-dark)"/>
        <stop offset="1" stop-color="#e8ece8"/>
      </linearGradient>
    </defs>
    <rect width="843" height="543" fill="url(#frontGreen)"/>
    <path d="M470,0 C420,120 500,260 450,380 C430,440 410,500 400,543 L430,543 C450,480 480,420 495,360 C530,240 450,110 520,0Z" fill="var(--green-deep)" opacity=".8"/>
    <path d="M492,0 C440,120 520,260 470,380 C450,440 430,500 420,543 L440,543 C462,480 490,420 505,360 C540,240 462,110 528,0Z" fill="#111"/>
    <path d="M504,0 C452,120 532,260 482,380 C462,440 442,500 432,543 L446,543 C470,480 498,420 513,360 C548,240 470,110 536,0Z" fill="var(--silver)"/>
    <path d="M530,0 L843,0 L843,543 L446,543 C470,480 498,420 513,360 C548,240 470,110 536,0Z" fill="url(#goldPhoto)" role="img" aria-label="Photo of an ornate gold bathroom faucet with crystal handles"/>
  </svg>
  <div class="brand">
    <div class="brand__name"><span class="brand__dot"></span>BRAMWELL</div>
    <div class="brand__sub">PLUMBING</div>
  </div>
  <p class="tagline tagline--dark">Our service is</p>
  <p class="tagline tagline--light">what set's us apart</p>
  <div class="front-call">CALL US: 561-555-0193</div>
  <div class="website">www.brwplumbing.example</div>
  <div class="license">License CFC9073651</div>
</section>

<section class="card card--back">
  <svg class="art" width="843" height="543" viewBox="0 0 843 543">
    <defs>
      <linearGradient id="tilePhoto" x1="0" y1="0" x2="1" y2="1">
        <stop offset="0" stop-color="var(--tile-light)"/>
        <stop offset="0.6" stop-color="#e4d2b3"/>
        <stop offset="1" stop-color="var(--tile-dark)"/>
      </linearGradient>
      <linearGradient id="backGreen" x1="0" y1="0" x2="1" y2="1">
        <stop offset="0" stop-color="var(--green-deep)"/>
        <stop offset="0.5" stop-color="var(--green-light)"/>
        <stop offset="1" stop-color="var(--green-mid)"/>
      </linearGradient>
    </defs>
    <rect width="520" height="543" fill="url(#tilePhoto)" role="img" aria-label="Photo of a polished nickel bridge kitchen faucet against cream tile with a decorative border"/>
    <path d="M0,420 C150,380 340,370 470,395 L470,543 L0,543Z" fill="url(#backGreen)"/>
    <path d="M0,420 C150,380 340,370 470,395" fill="none" stroke="var(--silver)" stroke-width="3"/>
    <path d="M540,0 C480,60 470,140 470,220 L470,543 L843,543 L843,0Z" fill="var(--white)"/>
    <path d="M520,0 L540,0 C480,60 470,140 470,220 L470,543 L455,543 C470,440 480,300 460,200 C450,120 470,50 520,0Z" fill="var(--white)"/>
    <path d="M480,0 C430,60 420,140 440,220 L455,220 C440,140 460,60 530,0Z" fill="var(--green-mid)"/>
    <path d="M530,0 C460,60 440,140 455,220 L463,220 C450,140 475,60 548,0Z" fill="#111"/>
    <path d="M548,0 C475,60 450,140 463,220 L469,220 C458,140 485,60 560,0Z" fill="var(--silver)"/>
    <path d="M560,0 C485,60 458,140 469,220 L470,543 L843,543 L843,0Z" fill="var(--white)"/>
    <path d="M470,500 C470,520 470,535 455,543 L470,543Z" fill="var(--green-mid)"/>
  </svg>
  <div class="call-badge">
    <span class="call-badge__label">CALL US:</span>
    <span class="call-badge__phone">561-555-0193</span>
  </div>
  <div class="brand">
    <div class="brand__name"><span class="brand__dot"></span>BRAMWELL</div>
    <div class="brand__sub">PLUMBING</div>
  </div>
  <div class="website">www.brwplumbing.example</div>
  <div class="postage">PRSRT STD<br>ECRWSS<br>U.S. POSTAGE<br>PAID<br>QPMX RETAIL</div>
  <div class="address">Local<br>Postal Customer</div>
</section>

</body>
</html>
```